Eco friendly Swedish beauty products sold in aluminum bottles - label design needed

We need help in designing a series of stick on labels for 80 ml (2.7 fl. oz.) aluminum bottles containing beauty products such as soaps, shampoo etc. The diameter of the bottle is 36 mm and the body of the bottles measures approx. 106 mm.
It is important for us that the label has a simplistic and clean feel with few colors (and the right ones!) and that the label helps amplify this product being both better and a more sustainable alternative to many of our plastic bottle competitors. The design and label should communicate the feel of an Eco-friendly, sustainable and modern brand of high quality - and with a Swedish concept.
We are using Montserrat font in our materials. Find attached information of preferred colors, the bottles and one example of our logotype. I am also available on e-mail should further information be needed.

Looking forward and very excited to receive your suggestions.
Note that we are expecting to start selling a series of approximately 10 different products where I will need one "master design" and then only smaller changes for each of the different products.

Target Market(s)

People whom are aware and not only look at price tag. Private and commercial market.

Industry/Entity Type

Beauty

Font styles to use
Other font styles liked:
• Montserrat

Requirements
Must have
• It must give the feel of being both better and a more sustainable alternative to many of our plastic bottle competitors.
Nice to have
• Simplistic. Clean. Clear.
Should not have
• Wrong colors, too complex designs.

```html
<!DOCTYPE html>
<html lang="en">
<head>
<meta charset="utf-8">
<title>Rena Holm – Shampoo label</title>
<link href="https://fonts.googleapis.com/css2?family=Montserrat:wght@400;500;600&family=Caveat:wght@500&display=swap" rel="stylesheet">
<style>
  :root {
    --canvas: #ffffff;
    --label: #e6e5e1;
    --olive-dark: #5d6d2a;
    --olive: #7b8a49;
    --olive-soft: #9aa474;
    --ink: #55612f;
    --white: #f4f4ef;
  }
  * { margin: 0; padding: 0; box-sizing: border-box; }
  html, body {
    width: 1200px; height: 1200px; overflow: hidden;
    background: var(--canvas);
    font-family: "Montserrat", sans-serif;
  }
  .label {
    position: absolute; left: 243px; top: 97px;
    width: 713px; height: 1006px;
    background: linear-gradient(90deg, #dcdbd6 0%, var(--label) 30%, #ecebe8 70%, #dedcd8 100%);
  }
  .rule {
    position: absolute; left: 0; width: 100%; height: 8px;
    background: var(--olive-dark);
  }
  .rule::before {
    content: ""; position: absolute; left: 0; right: 0; height: 14px;
    background: var(--olive-soft); opacity: .45;
  }
  .rule--top { top: 25px; }
  .rule--top::before { top: -25px; }
  .rule--bottom { top: 968px; }
  .rule--bottom::after {
    content: ""; position: absolute; left: 0; right: 0; top: 8px; height: 30px;
    background: #eceae6;
  }
  .brand-name {
    position: absolute; left: 0; top: 110px; width: 100%;
    font-weight: 500; font-size: 44px; letter-spacing: 4px;
    color: var(--olive); line-height: 1; text-align: center;
  }
  .product-name {
    position: absolute; left: 0; top: 512px; width: 100%;
    font-weight: 600; font-size: 76px; letter-spacing: 1px;
    color: var(--olive); line-height: 1; text-align: center;
  }
  .divider-dots {
    position: absolute; left: 339px; top: 608px;
    display: flex; gap: 6px;
  }
  .divider-dots span { width: 7px; height: 7px; border-radius: 50%; background: var(--olive-dark); }
  .claim {
    position: absolute; left: 120px; top: 667px; width: 474px; height: 86px;
    background: var(--olive);
    color: var(--white); font-weight: 400; font-size: 29px;
    display: flex; align-items: center; justify-content: center;
    letter-spacing: .3px;
  }
  .suitability {
    position: absolute; left: 166px; top: 790px; width: 380px;
    font-family: "Caveat", cursive; font-weight: 500; font-size: 52px;
    color: var(--ink); text-align: center; line-height: 1;
  }
  .suitability-line {
    position: absolute; left: 166px; top: 858px; width: 380px;
    border-top: 2px dashed var(--olive);
  }
  .volume {
    position: absolute; left: 0; top: 888px; width: 100%;
    font-weight: 500; font-size: 30px; color: var(--ink);
    text-align: center;
  }
</style>
</head>
<body>
  <main class="label">
    <div class="rule rule--top"></div>
    <p class="brand-name">RENA HOLM</p>
    <h1 class="product-name">SHAMPOO</h1>
    <div class="divider-dots"><span></span><span></span><span></span></div>
    <p class="claim">ALL NATURAL INGREDIENTS</p>
    <p class="suitability">for all hair type</p>
    <div class="suitability-line"></div>
    <p class="volume">200ml</p>
    <div class="rule rule--bottom"></div>
  </main>
</body>
</html>
```